Mediakit / brochure for Dutch Travel Blog

About our company:
• Bolderwijk.nl is a Travel- & influence network for independent travellers, outdoor geeks, culture lovers & adventure seekers.
• We don’t sell trips by ourself, we inspire other to travel.
• It’s all about travel inspiration.

About the media kit / brochure:
• The media kit itself must be a travel experience / inspiration.
• Colourful and clean design.
• Use the colours of our new logo
• Use our icons (marker, worldmap) in the design
• Use the style of our website.
• All the text in the media kit must be adjustable by us
• Page format: A4
• Number of pages: 6
• It must be printable as a brochure (for presentations)
• We also need a .pdf version of the brochure (for emailing it to our partners)
• Logo kit added: (1a) + (1b) + (1c) Logo sourcefile

Content of the media kit / brochure
• 6 pages
o (1) Front page
o (2) About Us
o (3) Stats / Companies work with
o (4) Advertising
o (5) Back page
o (6) Our contributors

• Example is attached: (2) example of a brochure with 5 pages A4 (don’t like the design of this example for our media kit, but just to show the idea of the 5 pages).

Maybe use a big travel photo that covers all pages?

For detailed information, I attached the document 'Design brochure Bolderwijk (version 2)'.
Updates

Hello designers,Small update for the Cover Page:- Please use one of the images from the attachment I added in the Brief Design: "URL of images for cover.txt"- Use this text "Travel- & influence network for independent travelers, outdoor geeks, culture lovers & adventure seekers."- Add the text MEDIA KIT (remove "2017: )Thanks.Hendrik Added Thursday, January 5, 2017

Target Market(s)

The mediakit / brochure is for our partners (travel organisations, airline companies, PR companies and big brands like Pale Timber Co and Vesko).

And the readers of our website are independent travellers, outdoor geeks and adventure seekers. So the theme of the Mediakit must be 'travel inspiration'.

Industry/Entity Type

Travel Industry

Requirements
Must have
• • The media kit itself must be a travel experience / inspiration.
• • Colourful and clean design.
• • Use the colours of our new logo
• • Use our icons (marker, worldmap) in the design
• • Use the style of our website.
• • All the text in the media kit must be adjustable by us
• • Page format: A4
• • Number of pages: 6
• • It must be printable as a brochure (for presentations)
• • We also need a .pdf version of the brochure (for emailing it to our partners)

```html
<!DOCTYPE html>
<html lang="en">
<head>
<meta charset="utf-8">
<title>Bolderwijk Media Kit</title>
<link href="https://fonts.googleapis.com/css2?family=Roboto:ital,wght@0,300;0,400;0,500;0,700;1,400;1,700&display=swap" rel="stylesheet">
<style>
:root{
  --pink:#e6407e;
  --green:#b5cc3a;
  --orange:#f5a623;
  --cyan:#3fb7e0;
  --teal:#39a9dc;
  --purple:#8e3c97;
  --dark:#3a3a3c;
  --yellow:#f6b531;
  --ink:#333;
  --muted:#666;
  --paper:#fff;
  --light:#f2f2f3;
  --bg:#a7a9ac;
}
*{box-sizing:border-box;margin:0;padding:0}
html,body{width:1200px;height:1081px;overflow:hidden;background:var(--bg);font-family:"Roboto",Arial,sans-serif;color:var(--ink)}
.canvas{position:relative;width:1200px;height:1081px}
.spread{position:absolute;left:36px;width:1117px;display:flex;box-shadow:2px 3px 6px rgba(0,0,0,.35);background:var(--paper)}
.spread--outside{top:35px;height:482px}
.spread--inside{top:564px;height:483px}
.panel{position:relative;width:372px;height:100%;overflow:hidden}
.panel--mid{width:373px}
.abs{position:absolute}
.stripe{height:4px;background:linear-gradient(90deg,var(--pink) 0 25%,var(--green) 25% 50%,var(--orange) 50% 75%,var(--cyan) 75% 100%)}
.url{font-size:10px;letter-spacing:3.2px;text-align:center;color:var(--ink)}
.rule{height:1px;background:var(--pink)}
.rule--orange{background:var(--orange)}
.map-fade{position:absolute;border-radius:45%;opacity:.35;background:radial-gradient(circle at 30% 40%,#f7b7cf 0,transparent 45%),radial-gradient(circle at 70% 35%,#bfe3f3 0,transparent 45%),radial-gradient(circle at 55% 75%,#f9dc9c 0,transparent 40%),radial-gradient(circle at 30% 80%,#d9e79a 0,transparent 35%)}

/* contributors */
.team-head{position:absolute;left:0;top:0;width:100%;height:63px;background:var(--dark);color:#fff;font-weight:700;font-size:13.5px;line-height:17px;text-align:center;padding-top:15px}
.team-head + .stripe{position:absolute;top:63px;left:0;width:100%}
.member{position:absolute;width:90px;margin-left:-45px;text-align:center;font-size:7px;color:var(--ink)}
.portrait{width:60px;height:60px;border-radius:50%;margin:0 auto 6px;background:linear-gradient(135deg,#c9a48a,#6b5446)}
.portrait--grey{background:linear-gradient(135deg,#ddd,#888)}
.mission{position:absolute;left:40px;width:292px;top:370px;text-align:center;font-style:italic;font-weight:700;font-size:11.5px;line-height:14px}

/* contact */
.panel--contact{background:var(--dark);color:#fff}
.city-fade{position:absolute;inset:0;background:linear-gradient(180deg,#4a4a4d 0%,#3d3d40 40%,#2f2f31 100%);opacity:.9}
.contact-card{position:absolute;left:29px;top:44px;width:224px;height:180px;background:var(--pink);padding:12px 18px 0 17px}
.contact-card h2{font-size:13.5px;font-weight:500;letter-spacing:.2px;padding-bottom:5px;border-bottom:1px solid rgba(255,255,255,.7)}
.contact{display:flex;align-items:center;gap:12px;font-size:9.5px;line-height:11.5px;padding:10px 0 8px;border-bottom:1px solid rgba(255,255,255,.7)}
.contact:last-child{border-bottom:0}
.card-corner{position:absolute;left:239px;top:178px;width:0;height:0;border-left:46px solid transparent;border-bottom:46px solid #2a2a2c}
.wordmark{display:flex;align-items:center;gap:6px;font-weight:700;color:#fff;letter-spacing:-.5px}
.wordmark .dot{width:.55em;height:.55em;border-radius:50%;background:var(--pink)}
.social{position:absolute;left:40px;top:342px;font-size:9px;line-height:16.6px;list-style:none}
.social li{display:flex;align-items:center;gap:10px}
.social .ic{width:11px;height:11px;border-radius:50%;border:1px solid var(--pink)}
.panel--contact .url{color:#fff;text-align:left}

/* cover */
.cover-photo{position:absolute;left:0;top:0;width:100%;height:333px;background:radial-gradient(ellipse at 50% 30%,#6fc84e 0,transparent 35%),radial-gradient(ellipse at 20% 60%,#4da23d 0,transparent 30%),linear-gradient(180deg,#3b2a57 0%,#2d3c5c 45%,#7f8ea1 75%,#cfd8e0 100%)}
.cover-band{position:absolute;left:0;top:333px;width:100%;height:46px;background:var(--pink);color:#fff;font-size:41px;line-height:46px;font-weight:300;padding-left:28px}
.cover-band b{font-weight:700}
.cover-band + .stripe{position:absolute;left:0;top:379px;width:100%}
.tagline{position:absolute;left:20px;width:332px;top:411px;text-align:center;font-size:13.5px;line-height:16px;color:var(--ink);font-weight:300}

/* inside */
.photo{position:absolute;background:linear-gradient(180deg,#d8a56b 0%,#8d7b86 40%,#4d5462 70%,#6b6f72 100%)}
.h-pink{color:var(--pink);font-weight:400;text-transform:uppercase}
.h-big{font-size:20px}
.h-mid{font-size:14px}
.h-teal{color:var(--teal);font-weight:400;font-size:12.5px}
.body{font-size:8.3px;line-height:10.4px;color:var(--ink)}
.panel--stats{background:var(--light)}
.label{font-size:10px;color:var(--orange)}
.stat-num{font-size:15px;color:var(--orange);font-weight:500}
.tiny{font-size:6.3px;color:var(--ink)}
.ages{position:absolute;left:111px;top:54px;list-style:none}
.ages li{display:flex;align-items:center;height:8.5px;font-size:5.5px;gap:3px}
.ages .bar{height:6.5px;color:#fff;padding-left:2px;line-height:6.5px}
.globe{position:absolute;left:24px;top:97px;width:75px;height:55px;border-radius:50%;background:radial-gradient(circle at 40% 40%,#7fd0ee,#2a9bd0)}
.partners{position:absolute;display:grid;gap:5px}
.logo-tile{background:#fff;border:1px solid #ddd;display:flex;align-items:center;justify-content:center;gap:4px;font-size:9px;font-weight:700;color:var(--ink)}
.logo-tile .mk{width:14px;height:14px;border-radius:50%;background:#ccc}
.pricing{position:absolute;left:188px;top:0;width:185px;height:167px;background:var(--yellow);padding:16px 10px 0 14px}
.pricing h3{font-weight:400;font-size:12.5px;color:var(--ink);margin-bottom:5px}
.price-table{width:100%;border-collapse:collapse;font-size:5.2px;font-weight:700}
.price-table td{border:1px solid #fff;padding:1.3px 2px;height:9.8px}
.price-table td:first-child{width:52%}
.offer{position:absolute;display:flex;gap:8px;width:170px}
.offer .ic{flex:0 0 11px;height:11px;border-radius:50%;border:1.5px solid var(--teal);margin-top:1px}
.offer h4{font-size:7.3px;font-weight:500;color:var(--ink)}
.offer p{font-size:6.2px;line-height:7.8px;color:var(--ink)}
.bottom-stripe{position:absolute;left:0;bottom:0;width:100%;height:7px;background:linear-gradient(90deg,var(--pink) 0 25%,var(--green) 25% 50%,var(--orange) 50% 75%,var(--cyan) 75% 100%)}
</style>
</head>
<body>
<div class="canvas">

  <!-- Outside spread: contributors, back, cover -->
  <section class="spread spread--outside">
    <article class="panel panel--team">
      <div class="map-fade" role="img" aria-label="Faint world map decoration" style="left:90px;top:250px;width:270px;height:230px"></div>
      <div class="team-head">Hi! We're all Bolderwijk and we want to<br>help you travel better…</div>
      <div class="stripe"></div>

      <div class="member" style="left:65px;top:85px"><div class="portrait" role="img" aria-label="Portrait of contributor"></div>Nadia Bakels</div>
      <div class="member" style="left:150px;top:85px"><div class="portrait" role="img" aria-label="Portrait of contributor"></div>Pieter Smulders</div>
      <div class="member" style="left:233px;top:85px"><div class="portrait" role="img" aria-label="Portrait of contributor"></div>Roos de Wit</div>
      <div class="member" style="left:308px;top:85px"><div class="portrait" role="img" aria-label="Portrait of contributor"></div>Roos de Wit</div>

      <div class="member" style="left:65px;top:170px"><div class="portrait" role="img" aria-label="Portrait of contributor"></div>Eva Brandsma</div>
      <div class="member" style="left:150px;top:170px"><div class="portrait" role="img" aria-label="Portrait of contributor"></div>Kees Wolters</div>
      <div class="member" style="left:233px;top:170px"><div class="portrait" role="img" aria-label="Portrait of contributor"></div>Hendrik Bakels</div>
      <div class="member" style="left:308px;top:170px"><div class="portrait portrait--grey" role="img" aria-label="Portrait of contributor"></div>Lotte Haverkamp</div>

      <div class="member" style="left:103px;top:262px"><div class="portrait" role="img" aria-label="Portrait of contributor"></div>Joris Meulman</div>
      <div class="member" style="left:186px;top:262px"><div class="portrait" role="img" aria-label="Portrait of contributor"></div>Femke van Dalen</div>
      <div class="member" style="left:270px;top:262px"><div class="portrait" role="img" aria-label="Portrait of contributor"></div>Ilse de Ruiter</div>

      <p class="mission">World Traveller with the mission to travel endlessly, write about their adventures and provide you with useful tips!</p>
      <div class="rule abs" style="left:114px;top:427px;width:144px"></div>
      <p class="url abs" style="left:0;width:100%;top:442px">www.bolderwijk.nl</p>
    </article>

    <article class="panel panel--mid panel--contact">
      <div class="city-fade" role="img" aria-label="Dimmed city skyline photograph"></div>
      <div class="contact-card">
        <h2>CONTACT INFORMATION</h2>
        <div class="contact">
          <svg width="13" height="14" viewBox="0 0 13 14"><circle cx="6.5" cy="4" r="3.2" fill="#fff"/><path d="M0 14c0-4 3-6 6.5-6S13 10 13 14z" fill="#fff"/></svg>
          <span>Person Name<br>name@bolderwijk.nl</span>
        </div>
        <div class="contact">
          <svg width="13" height="14" viewBox="0 0 13 14"><circle cx="6.5" cy="4" r="3.2" fill="#fff"/><path d="M0 14c0-4 3-6 6.5-6S13 10 13 14z" fill="#fff"/></svg>
          <span>Person Name<br>name@bolderwijk.nl</span>
        </div>
        <div class="contact">
          <svg width="13" height="14" viewBox="0 0 13 14"><circle cx="6.5" cy="4" r="3.2" fill="#fff"/><path d="M0 14c0-4 3-6 6.5-6S13 10 13 14z" fill="#fff"/></svg>
          <span>Person Name<br>name@bolderwijk.nl</span>
        </div>
      </div>
      <div class="card-corner"></div>

      <div class="wordmark abs" style="left:36px;top:276px;font-size:26px"><span>BOLDERWIJK</span><span class="dot"></span></div>

      <ul class="social">
        <li><span class="ic"></span>Chirper - chirper.com/bolderwijk</li>
        <li><span class="ic"></span>Pinnly - pinnly.com/bolderwijk</li>
        <li><span class="ic"></span>Vidstream - vidstream.com/bolderwijk</li>
        <li><span class="ic"></span>Friendbook - www.friendbook.com/bolderwijk</li>
        <li><span class="ic"></span>Snapgram - snapgram.com/bolderwijk</li>
      </ul>
      <div class="rule rule--orange abs" style="left:40px;top:433px;width:148px"></div>
      <p class="url abs" style="left:40px;top:444px">www.bolderwijk.nl</p>
    </article>

    <article class="panel panel--cover">
      <div class="cover-photo" role="img" aria-label="Northern lights over snowy mountains and an icy bay"></div>
      <div class="wordmark abs" style="left:0;width:100%;justify-content:center;top:48px;font-size:31px"><span>BOLDERWIJK</span><span class="dot"></span></div>
      <div class="cover-band"><b>2017</b> MEDIA KIT</div>
      <div class="stripe"></div>
      <p class="tagline">Dutch travel- &amp; influence network for independent travellers, outdoor geeks &amp; adventure seekers.</p>
      <div class="rule rule--orange abs" style="left:114px;top:446px;width:144px"></div>
      <p class="url abs" style="left:0;width:100%;top:457px">www.bolderwijk.nl</p>
    </article>
  </section>

  <!-- Inside spread: about, stats, advertising -->
  <section class="spread spread--inside">
    <article class="panel panel--about">
      <div class="photo" role="img" aria-label="Old city river bridge at sunset" style="left:0;top:0;width:372px;height:144px"></div>
      <div class="map-fade" role="img" aria-label="Faint world map decoration" style="left:140px;top:150px;width:230px;height:200px"></div>
      <h2 class="h-pink h-big abs" style="left:22px;top:182px">About us</h2>
      <p class="body abs" style="left:21px;top:215px;width:336px">Bolderwijk is leading in travel inspiration in The Netherlands. Our impassioned team of travel journalists, bloggers and youtubers create travel stories about independent &amp; off the beaten track travel, near and afar. Created in 2007, Bolderwijk began as a personal backpack blog that has now turned into an award winning travel platform.</p>
      <p class="body abs" style="left:21px;top:267px;width:336px">Our blog is all about providing inspiration for your own journeys no matter how big or small. We love documenting the world around us, seeking out eclectic travel moments and inspiring others to live the life they desire. Our knowledge of the world's most inspiring places is unrivalled.</p>
      <p class="body abs" style="left:21px;top:320px;width:178px">The travel stories by Bolderwijk show us that we can conquer the world, get lost in its beauty, and find ourselves wherever our feet (or passport) may take us. We take our readers and fans on a digital journey around the world in search of the beautiful, the unusual, the forgotten and the mundane. Sit down, relax and have a browse of our inspiring travel stories and videos on</p>
      <p class="abs" style="left:21px;top:420px;font-size:9.5px;letter-spacing:1.6px;color:var(--pink)">www.bolderwijk.nl</p>
      <div class="photo" role="img" aria-label="Riverside old town with church spire at dusk" style="left:204px;top:314px;width:152px;height:124px"></div>
    </article>

    <article class="panel panel--mid panel--stats">
      <div class="map-fade" role="img" aria-label="Faint world map decoration" style="left:150px;top:170px;width:220px;height:210px"></div>
      <h2 class="h-pink h-mid abs" style="left:24px;top:20px">Audience overview</h2>
      <span class="label abs" style="left:24px;top:37px">Gender</span>
      <svg class="abs" style="left:24px;top:51px" width="16" height="32" viewBox="0 0 16 32"><circle cx="8" cy="4" r="3.5" fill="var(--pink)"/><path d="M4 9h8l4 12H12v11H4V21H0z" fill="var(--pink)"/></svg>
      <span class="stat-num abs" style="left:44px;top:50px;color:var(--pink);font-size:12px">66%</span>
      <span class="stat-num abs" style="left:44px;top:65px;color:var(--teal);font-size:12px">34%</span>
      <svg class="abs" style="left:74px;top:51px" width="14" height="32" viewBox="0 0 14 32"><circle cx="7" cy="4" r="3.5" fill="var(--teal)"/><path d="M2 9h10v12h-2v11H4V21H2z" fill="var(--teal)"/></svg>
      <span class="label abs" style="left:111px;top:37px">Ages</span>
      <ul class="ages">
        <li><span class="bar" style="width:23px;background:#2bb04b">18 – 24</span>11%</li>
        <li><span class="bar" style="width:62px;background:var(--cyan)">25 – 34</span>30%</li>
        <li><span class="bar" style="width:75px;background:var(--purple)">35 – 44</span>36%</li>
        <li><span class="bar" style="width:25px;background:var(--pink)">45 – 54</span>12%</li>
        <li><span class="bar" style="width:19px;background:#ea4f3d">55 – 64</span>9%</li>
        <li><span class="bar" style="width:10px;background:var(--orange)">65+</span>2%</li>
      </ul>
      <div class="globe" role="img" aria-label="World globe illustration"></div>
      <span class="abs" style="left:108px;top:125px;font-size:22px;color:var(--teal);font-weight:500">81<small style="font-size:11px">%</small></span>
      <span class="label abs" style="left:131px;top:116px;line-height:11px;text-align:right">Countries<br>visited</span>

      <h2 class="h-pink h-mid abs" style="left:202px;top:20px">Traffic</h2>
      <svg class="abs" style="left:205px;top:38px" width="12" height="17" viewBox="0 0 12 17"><circle cx="6" cy="3" r="3" fill="var(--green)"/><path d="M1 7h10v5H9v5H3v-5H1z" fill="var(--green)"/></svg>
      <span class="tiny abs" style="left:225px;top:38px">Number of unique visitors each month:</span>
      <span class="stat-num abs" style="left:225px;top:47px">115,000</span>
      <svg class="abs" style="left:205px;top:65px" width="16" height="17" viewBox="0 0 16 17"><rect x="1" y="1" width="10" height="13" fill="none" stroke="var(--teal)" stroke-width="1.5"/><circle cx="10" cy="10" r="3" fill="none" stroke="var(--teal)" stroke-width="1.5"/><path d="M12 12l3 4" stroke="var(--teal)" stroke-width="1.5"/></svg>
      <span class="tiny abs" style="left:225px;top:64px">Number of page views each month:</span>
      <span class="stat-num abs" style="left:225px;top:73px;color:var(--teal)">240,000</span>

      <h2 class="h-pink h-mid abs" style="left:202px;top:100px">Social media</h2>
      <span class="abs" style="left:207px;top:123px;width:12px;height:12px;background:#3b5998"></span>
      <span class="stat-num abs" style="left:227px;top:118px">30,000</span>
      <span class="abs" style="left:283px;top:123px;width:12px;height:12px;background:#555"></span>
      <span class="stat-num abs" style="left:302px;top:118px">5200</span>
      <span class="abs" style="left:207px;top:145px;width:12px;height:12px;background:var(--teal)"></span>
      <span class="stat-num abs" style="left:227px;top:140px">7000</span>

      <h2 class="h-pink h-big abs" style="left:22px;top:175px">Companies we work with:</h2>
      <p class="body abs" style="left:22px;top:207px;width:332px;font-size:7px;line-height:8.6px">Wondering how to transform your product from a commodity into an experience? Not sure how to leverage the power of social media and connect with your target demographic? Need help aligning your branding with your company values? Whether you are a tourism board, travel company, personal brand or product, we can help. We work with more than 100 travel- and brand partners</p>

      <h3 class="h-teal abs" style="left:22px;top:255px">Brand partners</h3>
      <p class="body abs" style="left:22px;top:273px;width:150px;font-size:6.2px;line-height:8px">Bolderwijk reaches a niche audience of travellers passionate about unique experiences and amazing products. We have helped countless brands, from fashion labels to major technology corporations, bring their products to The Netherlands and reach their target consumers.</p>
      <div class="partners" style="left:22px;top:341px;grid-template-columns:62px 27px 38px;grid-auto-rows:28px">
        <div class="logo-tile">Kamvo</div>
        <div class="logo-tile" style="font-size:6.5px">Vesko</div>
        <div class="logo-tile" style="font-size:6.5px;line-height:7px;text-align:center">Pale Timber Co</div>
        <div class="logo-tile">Routewise</div>
        <div class="logo-tile" style="grid-column:span 2;width:38px"><span class="mk"></span></div>
      </div>

      <h3 class="h-teal abs" style="left:184px;top:255px">Travel partners</h3>
      <p class="body abs" style="left:184px;top:273px;width:170px;font-size:6.2px;line-height:8px">We have worked with some of the world's top travel companies &amp; destinations to help them achieve their goals. They leverage our authority and expertise in social media promotion, cross-marketing campaigns and unique content creation to showcase their offerings.</p>
      <div class="partners" style="left:184px;top:328px;grid-template-columns:73px 88px;grid-auto-rows:38px 44px 26px">
        <div class="logo-tile" style="color:#1a8fd1">Zuidair</div>
        <div class="logo-tile" style="color:#1a4b8e;font-size:8px">Lionport Airlines</div>
        <div class="logo-tile" style="color:#a5302f;font-size:8px">Tuktur Travel</div>
        <div class="logo-tile" style="color:#1a8fd1;font-size:11px">Isla Verano</div>
        <div class="logo-tile" style="color:#1a8fd1;font-weight:400">Flyscout</div>
        <div class="logo-tile" style="color:#1a4b8e;font-size:8px">Lynx Verre Reizen</div>
      </div>
      <p class="abs" style="left:22px;top:427px;font-size:15px;font-style:italic;font-weight:700;color:var(--orange)">Let's work together!</p>
    </article>

    <article class="panel panel--ads">
      <div class="map-fade" role="img" aria-label="Faint world map decoration" style="left:0;top:280px;width:220px;height:180px"></div>
      <h2 class="h-pink abs" style="left:23px;top:30px;font-size:20px">Advertising</h2>
      <p class="body abs" style="left:23px;top:62px;width:156px">Bolderwijk has a large online interactive community through its readers and social networks that provides a perfect venue to showcase your brand or destination to a highly engaged online audience of travel enthusiasts.</p>
      <p class="body abs" style="left:23px;top:130px;width:156px">Check out some of the things we can do for you.</p>

      <div class="pricing">
        <h3>Our Pricing:</h3>
        <table class="price-table">
          <tr><td>Traveldirectory</td><td>€ 100 (per year)</td></tr>
          <tr><td>Textlink</td><td>€ 250 (per year)</td></tr>
          <tr><td>Advertorials (max 3 links)</td><td>€ 500</td></tr>
          <tr><td>Sidebars</td><td>Please ask for current pricing</td></tr>
          <tr><td>Banners</td><td>Please ask for current pricing</td></tr>
          <tr><td>Social shares</td><td></td></tr>
          <tr><td>- Friendbook</td><td>€ 150</td></tr>
          <tr><td>- Snapgram</td><td>€ 100</td></tr>
          <tr><td>- Chirper</td><td>€ 50</td></tr>
          <tr><td>Reviews</td><td>€ 250</td></tr>
          <tr><td>Vidstream video</td><td>€ 250</td></tr>
          <tr><td>Videography using drones</td><td>€ 1.000</td></tr>
        </table>
      </div>

      <h3 class="h-teal abs" style="left:23px;top:174px;font-size:13px">Sponsorship Opportunities</h3>

      <div class="offer" style="left:23px;top:198px"><span class="ic"></span><div><h4>Travel Writing</h4><p>Yes please! Digital storytelling our core business. About independent &amp; off the beaten path travel. About exciting cities, with their buzzing street life, wild nightlife and unbeatable attractions. About otherworldly landscapes and awe-inspiring natural wonders. Near and afar.</p></div></div>
      <div class="offer" style="left:23px;top:272px"><span class="ic"></span><div><h4>Press &amp; Fam Trips</h4><p>The only thing we love more than experiencing new places is sharing the destinations with our readers. Our travel journalists are invited by tourist offices, airline companies, hotel brands and other partners. In 2016 for example our journalists went to Peru, Norway, South Africa, Costa Rica, Thailand and Spitsbergen.</p></div></div>
      <div class="offer" style="left:23px;top:338px"><span class="ic"></span><div><h4>Reviews / Sponsorship</h4><p>We love reviews! They give us a chance to let our readers know about unique products for the experiential traveler. We'd love to write an honest review for your app, product, hotel or anything else you can think of!</p></div></div>
      <div class="offer" style="left:23px;top:396px"><span class="ic"></span><div><h4>Travel logs</h4><p>Professionally produced and edited video logs. Showcase your destination through the</p></div></div>

      <div class="offer" style="left:194px;top:198px"><span class="ic"></span><div><h4>Travel directory</h4><p>Are you the owner of a small romantic B&amp;B in Italy? Or of that cool rafting company in Bali? Or do you have an excellent restaurant on a Caribbean island? We invented our unique traveldirectory for local companies, where we match accommodations, attractions, tours, travel companies and restaurants to a specific destination.</p></div></div>
      <div class="offer" style="left:194px;top:280px"><span class="ic"></span><div><h4>Advertising</h4><p>Advertorials, SEO articles, sidebars, banners, social media promotion. We have a lot of interesting advertising opportunities to help your business market its products and services to a target audience and help you expand your brand awareness.</p></div></div>
      <div class="offer" style="left:194px;top:345px"><span class="ic"></span><div><h4>Photography</h4><p>It's no secret that stunning images are one of the best and easiest ways to showcase your brand or destination. We offer a selection of photography services that help enhance your brands website and social networks.</p></div></div>
      <div class="offer" style="left:194px;top:404px"><span class="ic"></span><div><h4>Videography using drones</h4><p>Our state of the art drone footages will blow your mind.</p></div></div>

      <p class="abs" style="left:229px;top:453px;font-size:9.5px;letter-spacing:1.6px;color:var(--pink)">www.bolderwijk.nl</p>
    </article>
    <div class="bottom-stripe"></div>
  </section>

</div>
</body>
</html>
```